Website Redesign Brief for Breezeline Cooling Services WA

Creating a clear and concise brief for designers to redesign your website, https://breezelinecoolingwa.com.au/, is essential to ensure the project aligns with your vision for a more energetic, friendly, optimistic, and user-friendly website. Below is a sample brief tailored to your request, balancing specificity with flexibility to allow designers to bring their creativity to the table.

Website Redesign Brief for Breezeline Cooling WA
1. Project Overview

We are seeking a redesign of our website, https://breezelinecoolingwa.com.au/, to create a vibrant, engaging, and user-friendly online presence that reflects our brand’s commitment to providing top-notch air conditioning services in Western Australia. The redesigned website should feel energetic, friendly, and optimistic while maintaining professionalism and improving user experience.
2. Goals and Objectives

Enhance Brand Perception: Convey a modern, approachable, and positive brand identity that resonates with both residential and commercial clients.
Improve User Experience: Simplify navigation, improve accessibility, and ensure a seamless experience across devices (desktop, tablet, mobile).
Increase Engagement: Encourage visitors to explore services, request quotes, and contact us through clear calls-to-action (CTAs).
Boost Conversion Rates: Make it easier for users to find information and take action (e.g., booking services or inquiries).
Showcase Expertise: Highlight our professional air conditioning services, experience, and customer satisfaction in an inviting way.

3. Target Audience

Primary Audience: Homeowners and small business owners in Western Australia seeking air conditioning installation, maintenance, or repair services.
Secondary Audience: Property managers, commercial clients, and real estate professionals looking for reliable HVAC solutions.
Demographics: Ages 25–65, mix of tech-savvy and non-tech-savvy users, located primarily in Perth and surrounding areas.
User Needs: Clear information about services, transparent pricing, easy contact options, and reassurance of quality and reliability.

4. Design Preferences

Tone and Style:

Energetic: Use bold, vibrant colors (e.g., blues, whites, and pops of warm tones like orange or yellow) to evoke energy and optimism.
Friendly: Incorporate approachable language, welcoming imagery, and a clean, uncluttered layout.
Optimistic: Highlight positive customer outcomes (e.g., comfort, energy savings) through visuals and messaging.
Professional yet approachable: Maintain credibility as a trusted service provider while avoiding a cold or overly corporate feel.

Visual Elements:

Use high-quality images of happy customers, comfortable homes/offices, and modern air conditioning units.
Incorporate subtle animations or micro-interactions to add energy (e.g., hover effects on buttons or smooth scrolling).
Avoid overly complex graphics that may slow down the site or distract from usability.

Typography: Clean, modern fonts that are easy to read. Use larger, bold headings for hierarchy and warmth.
Inspiration: Websites like https://www.polarvane.com.au/ (clean and professional) or https://www.kestrelthermaltech.com.au/ (user-friendly and modern) but with a more vibrant and welcoming vibe.

5. Functional Requirements

User-Friendly Navigation: Simplify the menu structure to make key pages (e.g., Services, About Us, Contact) easily accessible.
Mobile Responsiveness: Ensure the site is fully optimized for mobile devices, with fast load times and intuitive touch interactions.
Key Features:

Prominent CTAs for requesting quotes, booking services, or contacting the team.
A clear service overview with icons or visuals for each service (e.g., installation, repairs, maintenance).
A testimonials section to showcase customer satisfaction.
An easy-to-use contact form with minimal fields.
Integration with Google Maps for location-based services or office directions.

SEO and Performance: Optimize for search engines (e.g., keywords like “air conditioning Perth”) and ensure fast loading speeds.
Accessibility: Follow WCAG guidelines to ensure the site is usable for all visitors, including those with disabilities.

6. Content Guidance

Existing Content: Review and refine current content from https://breezelinecoolingwa.com.au/ to make it concise, engaging, and aligned with the friendly tone.
New Content Ideas:

Add a “Why Choose Us” section highlighting expertise, customer service, and eco-friendly solutions.
Include a FAQ page to address common customer questions.
Create a blog section for tips on air conditioning maintenance or energy efficiency (optional).

Tone of Voice: Conversational, reassuring, and positive. Avoid technical jargon unless clearly explained.

7. Technical Considerations

Platform: Open to recommendations (e.g., WordPress, Wix, or custom-built) but prioritize ease of maintenance and scalability.
Integrations: Ensure compatibility with existing tools (e.g., Google Analytics, CRM for quote requests, or booking systems).
Domain and Hosting: Retain current domain (breezelinecoolingwa.com.au); hosting recommendations welcome.
Timeline: Initial design concepts within [insert timeline, e.g., 2–3 weeks], with full redesign completed by [insert deadline, e.g., 6–8 weeks].
Budget: [Insert budget range or state “flexible, please provide a quote”].

8. Deliverables

Wireframes and mockups for homepage, service pages, and contact page.
Fully responsive website design with all necessary pages.
Style guide (colors, fonts, imagery guidelines).
CMS setup (if applicable) with basic training for content updates.
Testing and optimization for performance and SEO.

9. Success Metrics

Increased time on site and reduced bounce rate.
Higher conversion rates for quote requests and contact form submissions.
Positive user feedback on ease of navigation and overall experience.
Improved search engine rankings for key terms within [insert timeframe, e.g., 3 months].

10. Additional Notes

Please provide a portfolio of similar projects or examples of user-friendly, vibrant websites.
We are open to creative suggestions to make the website stand out in the HVAC industry.
Regular progress updates and collaboration during the design process are appreciated.
Updates

designers are asking for more time

few have requested an extension. I Have extended

Target Market(s)

Primary Audience: Homeowners and small business owners in Western Australia seeking air conditioning installation, maintenance, or repair services. Secondary Audience: Property managers, commercial clients, and real estate professionals looking for reliable HVAC solutions. Demographics: Ages 25–65, mix of tech-savvy and non-tech-savvy users, located primarily in Perth and surrounding areas. User Needs: Clear information about services, transparent pricing, easy contact options, and reassurance of quality and reliability.

Industry/Entity Type

Air Conditioning and Refrigeration (HVAC & R)

Coding

Coded - Design and coding required

Colors
0054AA
0677BA
7BADD7
CADEEF
E8F1F8
59FF00
82FF00
B8FF75
E3FFCB
F4FFEA
F0912C
F2A743
F7CA91
FBE8D2
FDF5EE
EE7325
F08F49
F5BC92
FAE3D3
FDF4ED

Requirements
Must have
• Must have all my current information I currently have on my web page.
Nice to have
• A sales page for people to buy products online

```html
<!DOCTYPE html>
<html lang="en">
<head>
<meta charset="utf-8">
<title>Coolmere Air WA – Air Conditioning Perth</title>
<link href="https://fonts.googleapis.com/css2?family=Poppins:wght@400;500;600;700&display=swap" rel="stylesheet">
<style>
:root{
  --orange:#EE7325;
  --orange-dark:#d9611a;
  --ink:#111111;
  --text:#3a3a3a;
  --white:#ffffff;
  --sky:#E8F1F8;
  --peach:#FDF0E4;
  --peach-card:#FBE8D2;
}
*{box-sizing:border-box;margin:0;padding:0}
html,body{width:1200px;height:4180px;overflow:hidden}
body{font-family:'Poppins',sans-serif;color:var(--text);background:var(--white)}
a{text-decoration:none;color:inherit}
.btn{display:inline-block;background:var(--orange);color:var(--white);font-weight:600;font-size:13px;letter-spacing:.5px;padding:14px 28px;border-radius:30px;text-transform:uppercase;transition:background .2s}
.btn:hover{background:var(--orange-dark)}

/* header */
.site-header{height:132px;display:flex;align-items:center;justify-content:space-between;padding:0 96px 0 72px}
.brand{display:flex;align-items:center;gap:14px;font-weight:600;font-size:22px;color:var(--ink)}
.brand-dot{width:34px;height:34px;border-radius:50%;background:var(--orange)}
.nav{display:flex;align-items:center;gap:34px;font-size:15px;color:var(--ink)}
.nav a.active{color:var(--orange)}
.btn-outline{border:2px solid var(--ink);border-radius:30px;padding:10px 20px;font-weight:600;font-size:12px;letter-spacing:.5px}

/* hero */
.hero{height:508px;position:relative;background:linear-gradient(90deg,#120c08 0%,#1e140d 45%,#4a3a2c 70%,#6b5a48 100%);padding:104px 0 0 212px;color:var(--white)}
.hero-photo{position:absolute;right:0;top:0;width:560px;height:100%;background:linear-gradient(135deg,rgba(80,64,48,.2),rgba(190,170,140,.35))}
.hero h1{position:relative;font-size:46px;line-height:1.2;font-weight:600;width:560px}
.hero p{position:relative;margin:22px 0 40px;font-size:15px;line-height:1.6;width:520px}

/* about */
.about{height:768px;background:var(--sky);padding-top:76px}
.section-title{font-size:32px;font-weight:600;color:var(--ink);text-align:center;line-height:1.3}
.about-intro{width:620px;margin:22px auto 0;text-align:center;font-size:14px;line-height:1.6}
.about-row{display:flex;gap:20px;margin:44px 0 0 100px}
.about-photo{width:488px;height:420px;background:linear-gradient(160deg,#f2f2f2,#b9bcbf 60%,#6f6a66)}
.about-card{width:496px;height:308px;background:var(--peach-card);padding:38px 36px}
.about-card h3{font-size:22px;font-weight:600;color:var(--ink)}
.about-card p{font-size:14px;line-height:1.6;margin:18px 0 14px}

/* services */
.services{height:784px;background:var(--peach);padding-top:104px}
.eyebrow{font-size:12px;font-weight:500;letter-spacing:1px;text-transform:uppercase;color:var(--ink)}
.services .eyebrow{text-align:center}
.services .section-title{margin-top:12px}
.service-grid{position:relative;margin:60px 0 0 100px;height:416px}
.service-card{position:absolute;background:var(--white);padding:28px 24px}
.service-card h3{font-size:21px;font-weight:600;color:var(--ink)}
.service-card p{font-size:13px;line-height:1.55;margin:12px 0 20px}
.learn{font-size:13px;font-weight:500;color:var(--ink);display:inline-flex;align-items:center;gap:6px}
.service-photo{position:absolute}

/* cta */
.cta{height:428px;background:linear-gradient(120deg,#1b120c,#3a2b20 55%,#231912);display:flex;align-items:center;justify-content:center}
.cta-card{width:552px;height:244px;background:var(--white);text-align:center;padding-top:44px}
.cta-card h2{font-size:32px;font-weight:600;color:var(--ink)}
.cta-card p{font-size:14px;margin:10px 0 26px}

/* why */
.why{height:568px;background:var(--sky);padding:148px 100px 0}
.why h2{font-size:34px;font-weight:600;color:var(--ink);line-height:1.3;margin-top:14px;width:460px}
.why-grid{display:flex;gap:48px;margin-top:64px}
.why-item{width:300px}
.why-item h3{font-size:21px;font-weight:600;color:var(--ink)}
.why-item p{font-size:13px;line-height:1.6;margin-top:12px}

/* testimonials */
.testimonials{height:540px;background:var(--peach);padding-top:104px}
.testimonials .section-title{font-size:30px}
.quote-grid{display:flex;gap:44px;margin:44px 0 0 100px}
.quote-card{width:300px;height:300px;background:var(--white);text-align:center;padding-top:20px}
.avatar{width:72px;height:72px;border-radius:50%;margin:0 auto;background:linear-gradient(#c9c3bd,#7d756e)}
.quote-card h3{font-size:22px;font-weight:600;color:var(--ink);margin-top:16px}
.role{font-size:12px;margin-top:4px}
.quote-card p.quote{font-size:13px;line-height:1.6;margin:18px 28px 0}

/* contact */
.contact{height:380px;background:linear-gradient(120deg,#17110c,#2f241b 50%,#1c150f);color:var(--white);text-align:center;padding-top:98px}
.contact h2{font-size:32px;font-weight:600;line-height:1.3;width:560px;margin:0 auto}
.contact p{font-size:14px;line-height:1.6;width:600px;margin:18px auto 28px}

/* footer */
.site-footer{height:72px;display:flex;align-items:center;justify-content:space-between;padding:0 100px;font-size:14px;color:var(--ink)}
.footer-nav{display:flex;gap:22px}
.footer-nav a.active{color:var(--orange)}
</style>
</head>
<body>

<header class="site-header">
  <a class="brand" href="#"><span class="brand-dot"></span>Coolmere Air WA</a>
  <nav class="nav">
    <a class="active" href="#">Home</a><a href="#">About</a><a href="#">Services</a><a href="#">Blog</a><a href="#">Contact</a>
    <a class="btn-outline" href="#">REQUEST A QUOTE</a>
  </nav>
</header>

<section class="hero">
  <div class="hero-photo" role="img" aria-label="Photo of a bright modern living room with air conditioning"></div>
  <h1>Cool Comfort, Year-Round Happiness</h1>
  <p>Experience reliable air conditioning solutions tailored for your home, office, or industry. We're here to enhance your comfort all year round!</p>
  <a class="btn" href="#">Request a Quote</a>
</section>

<section class="about">
  <h2 class="section-title">Discover Our Passion For Climate<br>Control Solutions</h2>
  <p class="about-intro">At Coolmere Air WA, we prioritize our customers with expert service, ensuring comfort and efficiency in every installation and repair.</p>
  <div class="about-row">
    <div class="about-photo" role="img" aria-label="Photo collage of living spaces and technicians installing air conditioning units"></div>
    <div class="about-card">
      <h3>Our Journey In Air Conditioning</h3>
      <p>Founded with a vision to provide top-notch air conditioning services, Coolmere Air WA continues expertise with a commitment to customer satisfaction.</p>
      <p>We're a dedicated team passionate about creating optimal climates in homes and businesses across Perth.</p>
      <a class="btn" href="#">Read More</a>
    </div>
  </div>
</section>

<section class="services">
  <p class="eyebrow">Our Expertise</p>
  <h2 class="section-title">Comprehensive Air Conditioning<br>Services</h2>
  <div class="service-grid">
    <div class="service-card" style="left:0;top:0;width:300px;height:184px">
      <h3>Installation Services</h3>
      <p>Professional installation of various air conditioning systems.</p>
      <a class="learn" href="#">Learn More <svg width="10" height="10" viewBox="0 0 10 10"><path d="M3 1l4 4-4 4" fill="none" stroke="currentColor" stroke-width="1.6"/></svg></a>
    </div>
    <div class="service-card" style="left:332px;top:0;width:320px;height:208px">
      <h3>Repair Services</h3>
      <p>Expert repairs for all air conditioning brands and models.</p>
      <a class="learn" href="#">Learn More <svg width="10" height="10" viewBox="0 0 10 10"><path d="M3 1l4 4-4 4" fill="none" stroke="currentColor" stroke-width="1.6"/></svg></a>
    </div>
    <div class="service-photo" role="img" aria-label="Photo of a technician consulting with clients" style="left:668px;top:0;width:336px;height:208px;background:linear-gradient(150deg,#d9d4cf,#8f857c)"></div>
    <div class="service-photo" role="img" aria-label="Photo of a team working together in an office" style="left:0;top:184px;width:300px;height:232px;background:linear-gradient(150deg,#e6d2bb,#9a8470)"></div>
    <div class="service-card" style="left:332px;top:232px;width:320px;height:184px">
      <h3>Maintenance Services</h3>
      <p>Regular maintenance to keep your systems running smoothly.</p>
      <a class="learn" href="#">Learn More <svg width="10" height="10" viewBox="0 0 10 10"><path d="M3 1l4 4-4 4" fill="none" stroke="currentColor" stroke-width="1.6"/></svg></a>
    </div>
    <div class="service-card" style="left:668px;top:232px;width:336px;height:184px">
      <h3>Emergency Callouts</h3>
      <p>24/7 emergency air conditioning services when you need them most.</p>
      <a class="learn" href="#">Learn More <svg width="10" height="10" viewBox="0 0 10 10"><path d="M3 1l4 4-4 4" fill="none" stroke="currentColor" stroke-width="1.6"/></svg></a>
    </div>
  </div>
</section>

<section class="cta" role="img" aria-label="Darkened photo of a comfortable interior behind the call to action">
  <div class="cta-card">
    <h2>Get Started Today!</h2>
    <p>Reach out now for professional climate solutions designed just for you.</p>
    <a class="btn" href="#">Request a Quote</a>
  </div>
</section>

<section class="why">
  <p class="eyebrow">Why Choose Us</p>
  <h2>Unmatched Quality And Customer Care</h2>
  <div class="why-grid">
    <div class="why-item">
      <h3>Licensed Technicians</h3>
      <p>Our skilled technicians are fully licensed, ensuring safe and compliant installations and repairs for your peace of mind.</p>
    </div>
    <div class="why-item">
      <h3>Transparent Pricing</h3>
      <p>No hidden fees, just honest and fair pricing for every service we provide, tailored to meet your needs.</p>
    </div>
    <div class="why-item">
      <h3>Energy Efficiency Focus</h3>
      <p>We specialize in energy-efficient solutions that save you money while keeping your space comfortable year-round.</p>
    </div>
  </div>
</section>

<section class="testimonials">
  <h2 class="section-title">What Our Customers Say</h2>
  <div class="quote-grid">
    <div class="quote-card">
      <div class="avatar" role="img" aria-label="Customer portrait"></div>
      <h3>Liam Carver</h3><p class="role">Founder</p>
      <p class="quote">Coolmere Air WA was fantastic! They installed our system quickly and professionally. Highly recommended!</p>
    </div>
    <div class="quote-card">
      <div class="avatar" role="img" aria-label="Customer portrait"></div>
      <h3>Sophie Marlow</h3><p class="role">Founder</p>
      <p class="quote">The team at Coolmere Air WA provided exceptional service during our recent heatwave. So grateful for their prompt help!</p>
    </div>
    <div class="quote-card">
      <div class="avatar" role="img" aria-label="Customer portrait"></div>
      <h3>Daniel Reeves</h3><p class="role">Founder</p>
      <p class="quote">Great experience from start to finish! I trust Coolmere Air WA for all my air conditioning needs.</p>
    </div>
  </div>
</section>

<section class="contact" role="img" aria-label="Darkened photo of a cosy room behind the contact message">
  <h2>Contact Us For Quality Air Solutions Now!</h2>
  <p>Coolmere Air WA is your go-to partner for all air conditioning needs. We provide quality services that ensure comfort and satisfaction for every client.</p>
  <a class="btn" href="#">Request a Quote</a>
</section>

<footer class="site-footer">
  <nav class="footer-nav"><a class="active" href="#">Home</a><a href="#">About</a><a href="#">Services</a><a href="#">Blog</a><a href="#">Contact</a></nav>
  <p>Copyright © 2025 Coolmere Air WA</p>
</footer>

</body>
</html>
```